TernQuay Business Cards

Create business cards for our exciting new software company. We provide cloud billing systems and provisioning software for campany that need monthly SaaS and Cloud Billing

Target Market(s)

Enterprise businesses, b2b, telecom carriers, software manufactures

Industry/Entity Type

Software

```html
<!DOCTYPE html>
<html lang="en">
<head>
<meta charset="utf-8">
<title>TernQuay Business Card</title>
<link rel="stylesheet" href="https://fonts.googleapis.com/css2?family=Jost:wght@400&family=Tenor+Sans&display=swap">
<style>
  :root {
    --card-bg: #e9eef0;
    --brand-blue: #2f6fa6;
    --tagline-aqua: #5cc3d3;
    --name-navy: #132a63;
    --contact-teal: #5fb3c8;
    --web-aqua: #7fd3e0;
  }
  html, body {
    margin: 0;
    padding: 0;
    overflow: hidden;
    background: var(--card-bg);
  }
  .card {
    position: relative;
    width: 1200px;
    height: 741px;
    background: var(--card-bg);
    overflow: hidden;
  }
  .brand {
    position: absolute;
    left: 54px;
    top: 126px;
    display: flex;
    align-items: center;
    gap: 16px;
  }
  .brand-dot {
    width: 54px;
    height: 54px;
    border-radius: 50%;
    background: var(--brand-blue);
  }
  .brand-name {
    font-family: "Jost", sans-serif;
    font-weight: 400;
    font-size: 66px;
    line-height: 1;
    color: var(--brand-blue);
  }
  .tagline {
    position: absolute;
    right: 737px;
    top: 205px;
    margin: 0;
    text-align: right;
    font-family: "Jost", sans-serif;
    font-size: 17.5px;
    line-height: 20px;
    letter-spacing: 0.5px;
    text-transform: uppercase;
    color: var(--tagline-aqua);
  }
  .holder-name {
    position: absolute;
    left: 52px;
    top: 390px;
    margin: 0;
    font-family: "Tenor Sans", sans-serif;
    font-weight: 400;
    font-size: 66px;
    line-height: 1;
    letter-spacing: 5px;
    font-variant: small-caps;
    color: var(--name-navy);
  }
  .contact {
    position: absolute;
    left: 52px;
    margin: 0;
    line-height: 1;
    font-family: "Tenor Sans", sans-serif;
    color: var(--contact-teal);
  }
  .contact-phone {
    top: 508px;
    font-size: 56px;
    letter-spacing: 5px;
  }
  .contact-email {
    top: 580px;
    font-size: 50px;
    letter-spacing: 2px;
  }
  .contact-email .local {
    font-variant: small-caps;
    letter-spacing: 5px;
  }
  .contact-email .domain {
    font-family: "Jost", sans-serif;
    letter-spacing: 0;
  }
  .contact-web {
    top: 646px;
    font-size: 36px;
    letter-spacing: 5px;
    font-variant: small-caps;
    text-transform: lowercase;
    color: var(--web-aqua);
  }
</style>
</head>
<body>
  <main class="card">
    <div class="brand">
      <span class="brand-dot"></span>
      <span class="brand-name">TernQuay</span>
    </div>
    <p class="tagline">Cloud billing and<br>operational support systems</p>

    <h1 class="holder-name">Your Name Here</h1>

    <p class="contact contact-phone">P: 123456789</p>
    <p class="contact contact-email">E: <span class="local">yourname</span><span class="domain">@ternquay.com</span></p>
    <p class="contact contact-web">www.ternquay.com</p>
  </main>
</body>
</html>
```